Corvanta512 Business Card Redesign

I want to create a design for brand new business cards, I need something exceptional for clear plastic business card design. Please do not submit without it being on a clear design. Photos of the various logo versions attached.

```html
<!DOCTYPE html>
<html lang="en">
<head>
<meta charset="utf-8">
<title>Corvanta512 Business Card</title>
<link href="https://fonts.googleapis.com/css2?family=Montserrat:wght@400;500;600;700&display=swap" rel="stylesheet">
<style>
  :root {
    --navy: #143a72;
    --gold: #d4a22c;
    --gold-soft: #e3bb55;
    --card: #ffffff;
    --card-shade: #f1f1f1;
    --stage: #e4e4e6;
    --text: #1b3f78;
  }
  * { margin: 0; padding: 0; box-sizing: border-box; }
  html, body { width: 1200px; height: 901px; overflow: hidden; }
  body {
    background: var(--stage);
    font-family: "Montserrat", sans-serif;
    position: relative;
  }
  .card {
    position: absolute;
    left: 300px;
    width: 600px;
    height: 343px;
    border-radius: 18px;
    background: linear-gradient(160deg, var(--card) 55%, var(--card-shade));
    overflow: hidden;
    box-shadow: 0 6px 18px rgba(0,0,0,.18);
  }
  .card--front { top: 70px; }
  .card--back { top: 488px; }

  .band { position: absolute; left: 0; right: 0; bottom: 0; height: 26px; }
  .band__navy { position: absolute; left: 0; bottom: 0; height: 26px; width: 52%; background: var(--navy); }
  .band__gold { position: absolute; right: 0; bottom: 0; height: 26px; width: 48%; background: var(--gold); }
  .band__square {
    position: absolute; left: calc(52% - 9px); bottom: 4px;
    width: 18px; height: 18px; background: #fff;
  }

  .brand { position: absolute; display: flex; align-items: center; gap: 12px; }
  .brand__dot { width: 22px; height: 22px; border-radius: 50%; background: var(--navy); flex: none; }
  .brand__name {
    font-weight: 700; color: var(--gold); letter-spacing: 1px;
    font-size: 30px; text-transform: uppercase;
  }
  .card--front .brand { left: 34px; top: 150px; }
  .card--back .brand { left: 150px; top: 118px; }
  .card--back .brand__name { font-size: 38px; }

  .contact { position: absolute; left: 320px; top: 56px; color: var(--text); }
  .contact__name { font-weight: 700; font-size: 23px; line-height: 1.05; }
  .contact__role { color: var(--gold); font-weight: 500; font-size: 14px; margin-top: 2px; }
  .contact__rule { width: 16px; height: 2px; background: var(--gold); margin: 8px 0; }
  .contact__company { font-weight: 700; font-size: 13px; }
  .contact__address { font-weight: 500; font-size: 12.5px; line-height: 1.35; }
  .contact__list { list-style: none; margin-left: 0; }
  .contact__item { display: flex; align-items: center; gap: 10px; font-weight: 500; font-size: 13px; line-height: 1.6; }
  .contact__icon { width: 14px; height: 14px; flex: none; }

  .web {
    position: absolute; right: 40px; bottom: 46px;
    color: var(--gold); font-weight: 600; font-size: 17px; letter-spacing: 9px;
  }
</style>
</head>
<body>

<section class="card card--front">
  <div class="brand">
    <span class="brand__dot"></span>
    <span class="brand__name">Corvanta512</span>
  </div>

  <div class="contact">
    <div class="contact__name">Lucía Ferrand</div>
    <div class="contact__role">Legal Advisor</div>
    <div class="contact__rule"></div>
    <div class="contact__company">Corvanta512</div>
    <div class="contact__address">48 Harbor Lane Suite 210<br>Millbrook, CA 945120</div>
    <div class="contact__rule"></div>
    <ul class="contact__list">
      <li class="contact__item">
        <svg class="contact__icon" viewBox="0 0 16 16"><path fill="#d4a22c" d="M3.5 1.5l2.3 2.8-1.3 1.6c.9 2 2.6 3.7 4.6 4.6l1.6-1.3 2.8 2.3-1.5 2.3C6.6 13.4 2.6 9.4 1.2 3z"/></svg>
        (833) CRVN-512
      </li>
      <li class="contact__item">
        <svg class="contact__icon" viewBox="0 0 16 16"><rect x="1.5" y="3.5" width="13" height="9" fill="none" stroke="#d4a22c" stroke-width="1.6"/><path d="M1.5 3.5L8 9l6.5-5.5" fill="none" stroke="#d4a22c" stroke-width="1.6"/></svg>
        info@corvanta-512.com
      </li>
      <li class="contact__item">
        <svg class="contact__icon" viewBox="0 0 16 16"><circle cx="8" cy="8" r="6.5" fill="none" stroke="#d4a22c" stroke-width="1.6"/><path d="M1.5 8h13M8 1.5c-3 3.5-3 9.5 0 13M8 1.5c3 3.5 3 9.5 0 13" fill="none" stroke="#d4a22c" stroke-width="1.2"/></svg>
        www.corvanta-512.com
      </li>
    </ul>
  </div>

  <div class="band">
    <div class="band__navy"></div>
    <div class="band__gold"></div>
    <div class="band__square"></div>
  </div>
</section>

<section class="card card--back">
  <div class="brand">
    <span class="brand__dot"></span>
    <span class="brand__name">Corvanta512</span>
  </div>
  <div class="web">www.corvanta-512.com</div>
  <div class="band">
    <div class="band__navy"></div>
    <div class="band__gold"></div>
    <div class="band__square"></div>
  </div>
</section>

</body>
</html>
```